Vibrant business card design for Product person in Tech

I'm a 29 y/o female Product manager and I'd like to get a business card designed I can use when networking. I'd love something that stands out. Feel free to experiment with the use of colour, maybe geometrical elements - get creative! I work in the tech industry, so looking for a design without too much of a corporate feel. <br/><br/>The business card should have room for:<br/>Name<br/>Email address<br/>LinkedIn

Target Market(s)

Tech

Contact Information for Business Card

Name
Email
LinkedIn

Colors
faa54b
00a990
33b8a4
abd037
fbee3f
e667a6
ffcf3e
f59195

```html
<!DOCTYPE html>
<html lang="en">
<head>
<meta charset="utf-8">
<title>Dana Reyes – Business Card</title>
<link href="https://fonts.googleapis.com/css2?family=Cinzel:wght@400;500&display=swap" rel="stylesheet">
<style>
  :root {
    --backdrop: #8f8f8f;
    --card-white: #efeff1;
    --photo-plum: #4a3550;
    --photo-cream: #e9dccd;
    --photo-red: #8e1d34;
    --photo-amber: #e7a93a;
    --splash-orange: #f7844a;
    --splash-coral: #f0605a;
    --splash-pink: #e23f7c;
    --splash-violet: #9a5ccb;
    --ink-light: #ffffff;
  }
  * { box-sizing: border-box; margin: 0; padding: 0; }
  html, body {
    width: 1200px;
    height: 930px;
    overflow: hidden;
    background: var(--backdrop);
  }
  .canvas {
    position: relative;
    width: 1200px;
    height: 930px;
  }
  .card {
    position: absolute;
    left: 300px;
    width: 600px;
    height: 345px;
    border-radius: 22px;
    overflow: hidden;
    box-shadow: 0 6px 14px rgba(0,0,0,0.25);
  }
  .card--front { top: 90px; }
  .card--back  { top: 495px; background: var(--card-white); }

  .card__photo {
    width: 100%;
    height: 100%;
    background:
      radial-gradient(circle at 48% 45%, var(--photo-red) 0 11%, transparent 20%),
      radial-gradient(circle at 62% 28%, var(--photo-amber) 0 6%, transparent 14%),
      radial-gradient(circle at 80% 45%, #f4f1f4 0 12%, transparent 26%),
      linear-gradient(120deg, var(--photo-cream) 0%, #b7a3b8 30%, var(--photo-plum) 60%, #8b7391 100%);
  }

  .card__splash {
    position: absolute;
    left: 0; top: 0;
    width: 600px;
    height: 345px;
  }
  .card__details {
    position: absolute;
    left: 140px;
    top: 92px;
    width: 320px;
    text-align: center;
    color: var(--ink-light);
    font-family: "Cinzel", serif;
  }
  .card__name {
    font-size: 27px;
    font-weight: 500;
    letter-spacing: 1px;
  }
  .card__role {
    font-size: 17px;
    letter-spacing: 1px;
    margin-top: 2px;
  }
  .card__rule {
    width: 120px;
    height: 1px;
    background: var(--ink-light);
    margin: 14px auto 16px;
  }
  .card__contact {
    font-size: 16px;
    line-height: 1.45;
    letter-spacing: 0.5px;
  }
</style>
</head>
<body>
<main class="canvas">
  <section class="card card--front">
    <div class="card__photo" role="img" aria-label="Close-up photograph of colourful bottles and devices on a workbench"></div>
  </section>

  <section class="card card--back">
    <svg class="card__splash" viewBox="0 0 600 345" role="img" aria-label="Watercolour brush splash in orange, pink and violet">
      <defs>
        <linearGradient id="splashGradient" x1="0" y1="0" x2="1" y2="1">
          <stop offset="0" stop-color="var(--splash-orange)"/>
          <stop offset="0.4" stop-color="var(--splash-coral)"/>
          <stop offset="0.65" stop-color="var(--splash-pink)"/>
          <stop offset="1" stop-color="var(--splash-violet)"/>
        </linearGradient>
        <filter id="softEdge" x="-10%" y="-10%" width="120%" height="120%">
          <feGaussianBlur stdDeviation="3"/>
        </filter>
      </defs>
      <path fill="url(#splashGradient)" opacity="0.9" filter="url(#softEdge)"
        d="M172 62 C200 50 230 46 255 38 C290 30 320 44 350 36 C385 28 420 34 440 52
           C458 70 452 100 462 128 C474 160 466 190 470 220 C474 252 462 280 440 298
           C415 316 380 308 350 316 C320 324 290 312 262 318 C232 324 205 318 188 300
           C170 282 176 255 166 228 C156 200 168 170 160 140 C152 110 150 78 172 62 Z"/>
    </svg>
    <div class="card__details">
      <p class="card__name">Dana Reyes</p>
      <p class="card__role">Director</p>
      <div class="card__rule"></div>
      <p class="card__contact">info@danareyes.com<br>/dana/reyes.com</p>
    </div>
  </section>
</main>
</body>
</html>
```